Crestline Lending Group Business Cards

We are looking to revamp the current business cards each of our locations uses. We are a lending company that specializes in personal loans, title loans, and tax services. We have locations in New Mexico, Texas, and Oklahoma.

We would like a cleaner, sleeker look while still highlighting what we offer. Title Loans, Personal Loans & Tax Services. We also want to include our referral fee somewhere on the card. We would like to see an English option as well as a Spanish option for the cards.

PLEASE NOTE: Some business cards do not include the employee's name but just the store's location, while others will include both.

These are double-sided business cards, and we would like to see proof if possible. I have included proofs of our current business cards for you to review below, as well as our company logo. Feel free to get creative with the logo, etc! Colors should match the logo; however, you do not need to use all of our logo colors if you don't want to.

```html
<!DOCTYPE html>
<html lang="en">
<head>
<meta charset="utf-8">
<title>Crestline Lending Group Business Cards</title>
<link href="https://fonts.googleapis.com/css2?family=Open+Sans:wght@400;600;700;800&display=swap" rel="stylesheet">
<style>
  :root {
    --backdrop: #222222;
    --paper: #fdfdf5;
    --brand-green: #10512f;
    --brand-red: #c62a2a;
    --ink: #1b1b1b;
    --white: #ffffff;
  }
  * { margin: 0; padding: 0; box-sizing: border-box; }
  html, body {
    width: 1200px; height: 780px; overflow: hidden;
    background: var(--backdrop);
    font-family: "Open Sans", Arial, sans-serif;
  }
  .card {
    position: absolute;
    width: 560px; height: 320px;
    top: 230px;
    box-shadow: 0 10px 30px rgba(0,0,0,.5);
  }
  .card-front { left: 25px; background: var(--paper); color: var(--ink); }
  .card-back {
    left: 615px; background: var(--brand-green);
    display: flex; align-items: center; justify-content: center;
  }

  .name-block {
    position: absolute; top: 22px; left: 0;
    padding-left: 22px;
    border-left: 10px solid var(--brand-red);
  }
  .person-name { font-size: 26px; font-weight: 800; line-height: 1; }
  .person-name .first { color: var(--brand-red); }
  .person-name .last { color: var(--brand-green); }
  .person-title { font-size: 12px; margin-top: 3px; }

  .addresses {
    position: absolute; top: 96px; left: 32px;
    font-size: 12.5px; line-height: 1.3;
  }
  .address + .address { margin-top: 4px; }

  .contact-list {
    position: absolute; top: 168px; left: 32px;
    list-style: none; font-size: 12.5px; line-height: 1.45;
  }
  .contact-list li { display: flex; align-items: center; gap: 7px; }
  .contact-list svg { width: 11px; height: 11px; fill: var(--brand-red); flex: none; }

  .company-name {
    position: absolute; top: 96px; right: 34px; width: 240px;
    text-align: center;
    font-size: 30px; font-weight: 700; line-height: 1.1;
    color: var(--brand-green);
  }

  .services {
    position: absolute; bottom: 24px; left: 200px;
    list-style: none; font-size: 13.5px; line-height: 1.4;
  }
  .services li::before {
    content: ""; display: inline-block;
    width: 7px; height: 7px; border-radius: 50%;
    background: var(--brand-green);
    margin-right: 8px; vertical-align: middle;
  }

  .referral {
    position: absolute; bottom: 20px; right: 32px;
    text-align: left;
  }
  .referral-lead { font-size: 14px; }
  .referral-offer { display: flex; align-items: flex-end; gap: 6px; }
  .referral-get { font-size: 30px; font-weight: 800; color: var(--brand-green); line-height: 1; }
  .referral-upto { font-size: 10px; font-weight: 700; color: var(--brand-green); line-height: 1.05; }
  .referral-amount { font-size: 34px; font-weight: 800; color: var(--brand-red); line-height: 1; }

  .back-name {
    font-size: 44px; font-weight: 700; line-height: 1.1;
    color: var(--white); text-align: center; width: 420px;
  }
</style>
</head>
<body>
  <section class="card card-front" aria-label="Business card front">
    <div class="name-block">
      <p class="person-name"><span class="first">Jane</span> <span class="last">Doe</span></p>
      <p class="person-title">Branch Manager</p>
    </div>

    <div class="addresses">
      <p class="address">48 Juniper Avenue, Suite C,<br>Riverbend, Texas 75012</p>
      <p class="address">910 Harlow Road<br>Riverbend, Texas 75012</p>
    </div>

    <ul class="contact-list">
      <li><svg viewBox="0 0 24 24" aria-hidden="true"><path d="M6.6 10.8a15.1 15.1 0 0 0 6.6 6.6l2.2-2.2a1 1 0 0 1 1-.25 11.4 11.4 0 0 0 3.6.57 1 1 0 0 1 1 1V20a1 1 0 0 1-1 1A17 17 0 0 1 3 4a1 1 0 0 1 1-1h3.5a1 1 0 0 1 1 1c0 1.25.2 2.45.57 3.57a1 1 0 0 1-.25 1z"/></svg>(575) 555-0148</li>
      <li><svg viewBox="0 0 24 24" aria-hidden="true"><circle cx="12" cy="12" r="10"/></svg>www.crestlinelending.com</li>
      <li><svg viewBox="0 0 24 24" aria-hidden="true"><path d="M2 5h20v14H2z M2 5l10 8 10-8"/></svg>abcde@crestlinelending.com</li>
    </ul>

    <p class="company-name">Crestline Lending Group</p>

    <ul class="services">
      <li>Title Loans</li>
      <li>Tax Services</li>
      <li>Personal Loans</li>
    </ul>

    <div class="referral">
      <p class="referral-lead">Refer a Friend</p>
      <div class="referral-offer">
        <span class="referral-get">GET</span>
        <span class="referral-upto">UP<br>TO</span>
      </div>
      <p class="referral-amount">$100</p>
    </div>
  </section>

  <section class="card card-back" aria-label="Business card back">
    <p class="back-name">Crestline Lending Group</p>
  </section>
</body>
</html>
```